Marlow Bridge needs a brochure review

We are a company operating in more than 10 countries that, since 1972, has the ambitious and innovative objective to stimulate foreign language learning by discovering different countries and cultures, through training courses tailored to individual needs
We need a layout review of our brochure in order to make the content clearer, immediate and appealing and, at the same time, make the layout more modern and young.
The pages we need are: the cover and pages 3, 5, 7, 20, 21, 22, 23, 34, 36, 37. You will find our actual brochure pdf as attachment

Target Market(s)

Students and families, business

Industry/Entity Type

It Company

Requirements
Must have
• The same written information as the actual one.
• Blue and green colours.
• The cover must be simple, elegant and clean but new and effective. In addition to the cover the pages you should review are number :2, 3, 4, 5, 6, 7. Feel free to use new background, images and new layout for the text.

```html
<!DOCTYPE html>
<html lang="it">
<head>
<meta charset="utf-8">
<title>Marlow Bridge Academy – Che fa per te</title>
<link href="https://fonts.googleapis.com/css2?family=Alegreya+Sans+SC:wght@400;500&display=swap" rel="stylesheet">
<style>
  :root {
    --green: #78b843;
    --green-light: #a6d870;
    --blue: #1c5d9c;
    --ink: #1b1b1b;
    --mist: #eef3f1;
  }
  html, body { margin: 0; padding: 0; overflow: hidden; }
  body { width: 976px; height: 1200px; background: #fff; }
  .page {
    position: relative; width: 976px; height: 1200px; overflow: hidden;
    font-family: "Alegreya Sans SC", sans-serif; color: var(--ink);
  }
  .backdrop {
    position: absolute; inset: 0;
    background:
      radial-gradient(ellipse at 80% 10%, rgba(150,185,150,.45), transparent 55%),
      radial-gradient(ellipse at 85% 85%, rgba(150,185,170,.45), transparent 55%),
      linear-gradient(180deg, #e4ece6 0%, #f4f7f6 30%, #f6f8f8 60%, #e6eeec 100%);
  }
  .brand-band { position: absolute; left: 344px; top: 40px; width: 590px; height: 46px; }
  .brand-name {
    position: absolute; right: 56px; top: 50px; margin: 0;
    color: #fff; font-size: 23px; font-weight: 400; letter-spacing: .3px;
  }
  .title {
    position: absolute; left: 40px; top: 136px; margin: 0;
    font-size: 53px; font-weight: 400; letter-spacing: 1.5px; line-height: 1;
  }
  .section-head {
    position: absolute; left: 40px; margin: 0;
    color: var(--green); font-size: 27px; font-weight: 400; line-height: 1;
  }
  .body-copy {
    position: absolute; left: 40px; margin: 0; white-space: nowrap;
    font-size: 19.5px; line-height: 17.9px; letter-spacing: .2px;
  }
  .photo { position: absolute; box-shadow: 0 0 10px 6px rgba(255,255,255,.85); }
  .photo-field { left: 382px; top: 260px; width: 226px; height: 200px;
    background: linear-gradient(180deg, #1d3552 0%, #35507a 45%, #4f8a3a 70%, #6ca84a 100%); }
  .photo-drama { left: 382px; top: 480px; width: 238px; height: 188px;
    background: linear-gradient(180deg, #e6e4e2 0%, #cfc8c2 40%, #2a2a30 100%); }
  .photo-campus { left: 636px; top: 228px; width: 292px; height: 352px;
    background: linear-gradient(180deg, #2f6fd0 0%, #6d9ee0 35%, #a9593e 62%, #b86a4a 75%, #5d8f3c 100%); }
  .photo-match { left: 668px; top: 608px; width: 240px; height: 184px;
    background: linear-gradient(180deg, #8a7a6a 0%, #b7a995 40%, #6f9a46 70%, #5f8a38 100%); }
  .offer {
    position: absolute; left: 488px; top: 862px; margin: 0; white-space: nowrap;
    color: var(--blue); font-size: 20px; line-height: 18px;
  }
  .venues {
    position: absolute; left: 472px; top: 954px; margin: 0; padding: 0; list-style: none;
    color: var(--blue); font-size: 22px; line-height: 21.5px;
  }
  .venues li::before { content: "•"; display: inline-block; width: 16px; font-size: 16px; }
  .footnote {
    position: absolute; left: 488px; top: 1050px; margin: 0; white-space: nowrap;
    color: var(--blue); font-size: 14px; line-height: 12px;
  }
  .folio {
    position: absolute; right: 56px; top: 1145px; margin: 0;
    font-size: 20px; line-height: 1;
  }
</style>
</head>
<body>
<div class="page">
  <div class="backdrop" role="img" aria-label="Faded photo of a large waterfall and river landscape"></div>

  <svg class="brand-band" viewBox="0 0 590 46" aria-hidden="true">
    <defs>
      <linearGradient id="bandGrad" x1="0" x2="1" y1="0" y2="0">
        <stop offset="0" stop-color="#78b843" stop-opacity="0"/>
        <stop offset=".25" stop-color="#78b843" stop-opacity=".75"/>
        <stop offset="1" stop-color="#5fae2e"/>
      </linearGradient>
    </defs>
    <path d="M0 14 Q150 4 300 8 T590 4 L588 40 Q440 46 300 42 T0 38 Z" fill="url(#bandGrad)"/>
  </svg>
  <p class="brand-name">Marlow Bridge Academy</p>

  <h1 class="title">CHE FA PER TE</h1>

  <h2 class="section-head" style="top:272px">Programma</h2>
  <p class="body-copy" style="top:306px">Sport Academy unisce al corso<br>di lingua sessioni pomeridiane<br>di calcio e di rugby, ognuna<br>della durata di 3 ore. Durante<br>gli allenamenti, tutti rigoro-<br>samente in lingua inglese, con<br>la guida esperta di un Team<br>Leader, coach professionista,<br>e dei suoi assistenti, ci<br>saranno momenti di<br>formazione specifica per<br>ciascuna tattica e disciplina.<br>I ragazzi saranno divisi per<br>gruppi di pari età e abilità, così<br>da garantire a ogni allievo<br>l'effettivo miglioramento<br>delle sue competenze sportive<br>e linguistiche. Perché è<br>scientificamente provato che<br>apprendimento fa rima con<br>divertimento...</p>

  <h2 class="section-head" style="top:696px">Football</h2>
  <p class="body-copy" style="top:729px">Ogni sessione sarà incentrata<br>su una tecnica diversa per<br>acquisire una conoscenza<br>completa di tutte le tattiche di<br>gioco: i ragazzi impareranno i<br>trucchi di dribbling, passaggio,<br>tiro e controllo palla e metter-<br>ranno in practica le proprie<br>abilità con partite e tornei.</p>

  <h2 class="section-head" style="top:910px">Rugby</h2>
  <p class="body-copy" style="top:951px">Guidati da intruttori esperti, i<br>ragazzi aprenderanno le<br>tecniche del rugby e le<br>modalità di gioco. Dopo ogni<br>sessione avranno modo di<br>allenarsi per testare le loro<br>capacità e potranno cimentarsi<br>in vere partite.</p>

  <div class="photo photo-field" role="img" aria-label="Floodlit sports field at dusk with players training"></div>
  <div class="photo photo-drama" role="img" aria-label="Students rehearsing a group exercise with poles in a studio"></div>
  <div class="photo photo-campus" role="img" aria-label="Red brick campus building with glass dome under blue sky and autumn trees"></div>
  <div class="photo photo-match" role="img" aria-label="Young players in helmets running with the ball on a grass pitch"></div>

  <p class="offer">Sport Academy, il programma<br>per migliorare il tuo inglese,<br>è disponibile al costo di €50<br>a settimana* a:</p>
  <ul class="venues">
    <li>Chelmsford</li>
    <li>Loughborough</li>
    <li>Effingham</li>
    <li>Windsor</li>
  </ul>
  <p class="footnote">*in omaggio per le prenotazioni<br>effettuate entro il 10/03/2017</p>

  <p class="folio">Marlow Bridge Estate 2017 - 7</p>
</div>
</body>
</html>
```